Career-focused learning application platform

We have a K-12 learning application platform designed for grades 6-12 that needs user interface improvements that provide a positive experience for all users (teachers and students). The learning platform provides career-focused math curriculum and career exploration resources. We would like to improve the user-interface with engaging design elements without taking away from the functionality and performance of the platform.

```html
<!DOCTYPE html>
<html lang="en">
<head>
<meta charset="utf-8">
<title>Routewise – Learning Platform Screens</title>
<link href="https://fonts.googleapis.com/css2?family=Roboto:wght@400;500;700&display=swap" rel="stylesheet">
<style>
:root{
  --board:#efefef;
  --purple:#2a1554;
  --indigo:#4b4a93;
  --violet:#5552b0;
  --orange:#f7861b;
  --orange-dark:#d9690b;
  --peach:#fde9d3;
  --lavender:#dedcf6;
  --lilac:#e4e3f7;
  --aqua:#cdfbf7;
  --teal:#1f6e66;
  --teal-ring:#1a7a6e;
  --ink:#1d1d1f;
  --muted:#6b6b75;
  --red:#e5262b;
  --field:#f1f1f3;
  --white:#fff;
}
*{margin:0;padding:0;box-sizing:border-box}
html,body{width:1200px;height:1200px;overflow:hidden;background:var(--board);font-family:'Roboto',sans-serif;color:var(--ink)}
.board{position:absolute;left:0;top:0;width:1932px;height:1932px;transform:scale(.62112);transform-origin:0 0}
.abs{position:absolute}
.shadow{box-shadow:0 10px 30px rgba(40,30,80,.16)}

/* brand */
.brand{position:absolute;display:flex;align-items:center;gap:5px;color:var(--orange);font-weight:700;font-size:12px;letter-spacing:.5px}
.brand-dot{width:13px;height:13px;border-radius:50%;background:var(--orange)}

/* app chrome */
.app{position:absolute;background:var(--purple);overflow:hidden}
.app-main{position:absolute;right:0;bottom:0;background:var(--white);border-top-left-radius:30px}
.search{position:absolute;height:13px;border-radius:7px;background:var(--white);font-size:4.5px;color:#555;padding:0 8px;display:flex;align-items:center;justify-content:space-between}
.search svg{width:6px;height:6px}
.avatar{position:absolute;width:21px;height:21px;border-radius:50%;background:radial-gradient(circle at 50% 40%,#e8c3a8,#8a5a3c);border:1.5px solid #fff}
.email{position:absolute;color:var(--white);font-size:10px}
.nav-item{position:absolute;left:5px;width:94px;height:25px;display:flex;align-items:center;gap:7px;padding-left:15px;font-size:6px;color:var(--white);letter-spacing:.3px}
.nav-item svg{width:8px;height:8px;flex:none}
.nav-item.is-active{background:var(--orange);border-radius:13px 0 0 13px}

/* dashboard */
.dash{position:absolute;width:593px;height:818px}
.dash--compact{transform:scale(.9663);transform-origin:0 0}
.section-title{position:absolute;font-size:9px;font-weight:700}
.stat{position:absolute;top:86px;width:133px;height:82px;border-radius:6px}
.stat-label{position:absolute;left:8px;top:10px;font-size:9px}
.stat-value{position:absolute;left:20px;top:38px;font-size:30px;font-weight:500}
.stat-ring{position:absolute;right:7px;top:18px;width:56px;height:56px}
.stat-ring span{position:absolute;inset:0;display:flex;align-items:center;justify-content:center;font-size:13px}
.stat--done{background:var(--peach);color:var(--orange)}
.stat--taken{background:var(--lavender);color:var(--indigo)}
.stat--passed{background:var(--aqua);color:var(--teal-ring)}
.stat .stat-value{color:var(--ink)}
.spotlight{position:absolute;left:132px;top:230px;width:214px;height:138px;background:#fff;border-radius:4px;box-shadow:0 6px 18px rgba(247,134,27,.18);overflow:hidden}
.spotlight-head{height:23px;background:var(--orange);color:#fff;font-size:7px;font-weight:500;display:flex;align-items:center;justify-content:space-between;padding:0 8px 0 14px}
.spotlight-body{padding:8px 13px;font-size:4.6px;line-height:1.35}
.spotlight-body h4{font-size:5.5px;margin:4px 0 3px}
.earnings{display:flex;gap:22px;margin-top:4px}
.earnings div{font-size:5px}
.earnings b{display:block;font-weight:400;font-size:6.5px;margin-top:3px}
.video{position:absolute;left:359px;top:230px;width:214px;height:138px;border-radius:4px;background:linear-gradient(135deg,#5a5e66,#2f3138 55%,#9da1a8);overflow:hidden}
.play{position:absolute;left:50%;top:50%;width:46px;height:46px;margin:-23px 0 0 -23px}
.class-card{position:absolute;top:426px;width:133px;height:147px;background:#fff;border-radius:4px;box-shadow:0 4px 14px rgba(0,0,0,.1)}
.class-teacher{position:absolute;left:12px;top:11px;font-size:6.5px;color:var(--teal);font-weight:500}
.class-period{position:absolute;right:10px;top:12px;font-size:5px}
.folder-back{position:absolute;left:20px;top:62px;width:93px;height:74px;background:var(--orange-dark);border-radius:4px}
.folder-paper{position:absolute;left:26px;top:36px;width:81px;height:54px;border-radius:3px;color:#fff;font-size:7px;font-weight:500;text-align:center;padding-top:10px;line-height:1.3}
.paper-teal{background:var(--teal)}
.paper-indigo{background:var(--indigo)}
.folder-front{position:absolute;left:20px;top:74px;width:93px;height:62px;background:var(--orange);border-radius:0 0 4px 4px;clip-path:polygon(0 14%,48% 14%,60% 0,100% 0,100% 100%,0 100%);color:#fff;font-size:6.5px;font-weight:500;display:flex;align-items:flex-end;justify-content:center;padding-bottom:20px;letter-spacing:.3px}
.lesson-table{position:absolute;left:127px;top:637px;width:450px;border-collapse:collapse;font-size:5.5px}
.lesson-table th{background:var(--orange);color:#fff;height:38px;text-align:left;font-weight:500;padding-left:16px;border-right:1px solid #fbb46f}
.lesson-table th:last-child{border-right:0}
.lesson-table td{height:19.5px;padding-left:16px;border-right:1px solid #e6e6ea}
.lesson-table td:last-child{border-right:0;color:var(--red)}
.lesson-table tr:nth-child(odd) td{background:#f5f5fa}

/* sign in */
.signin{position:absolute;left:65px;top:323px;width:591px;height:333px;background:#fff;overflow:hidden}
.signin-bar{position:absolute;left:0;top:0;width:100%;height:52px;border-bottom:1.5px solid #c9c9cf}
.btn{position:absolute;height:22px;border-radius:3px;color:#fff;font-size:8px;display:flex;align-items:center;justify-content:center;letter-spacing:.3px}
.signin-title{position:absolute;left:0;top:85px;width:290px;text-align:center;font-size:13px;font-weight:700;line-height:16px}
.tiny{position:absolute;font-size:5px;text-align:center}
.provider{position:absolute;top:146px;height:25px;background:#fff;box-shadow:0 2px 6px rgba(0,0,0,.14);border-radius:2px;display:flex;align-items:center;gap:8px;padding-left:10px;font-size:5.5px}
.provider i{width:12px;height:12px;border-radius:50%;background:var(--violet);display:block}
.field{position:absolute;left:43px;width:205px;height:27px;background:var(--field);border-radius:2px;border-bottom:1px solid #ddd;font-size:5px;color:#888;padding:11px 0 0 11px}
.art{position:absolute}

/* class page */
.back{position:absolute;display:flex;align-items:center;gap:5px;font-size:5px;font-weight:500}
.back svg{width:14px;height:6px}
.course-head{position:absolute;left:115px;top:86px;width:463px;height:77px;background:linear-gradient(90deg,#fde3bf,#fdebd6);border-radius:4px 4px 0 0}
.ghost-btn{position:absolute;top:101px;width:79px;height:21px;background:#fff;border-radius:3px;box-shadow:0 2px 6px rgba(0,0,0,.12);font-size:5px;display:flex;align-items:center;justify-content:center;gap:4px}
.ghost-btn svg{width:9px;height:9px}
.lessons-panel{position:absolute;left:115px;top:163px;width:463px;height:170px;background:#fff;box-shadow:0 4px 12px rgba(0,0,0,.12)}
.lesson-row{position:absolute;left:133px;width:440px;height:20px}
.lesson-thumb{position:absolute;left:0;top:2px;width:14px;height:14px;background:linear-gradient(180deg,var(--teal) 55%,var(--orange) 55%);border-radius:1px}
.lesson-name{position:absolute;left:27px;top:0;font-size:5.2px;font-weight:700}
.lesson-desc{position:absolute;left:27px;top:7px;font-size:4.5px;white-space:nowrap}
.lesson-due{position:absolute;left:378px;top:0;font-size:4.5px;font-weight:700}
.begin{position:absolute;left:378px;top:8px;width:46px;height:8px;background:var(--violet);color:#fff;font-size:4px;display:flex;align-items:center;justify-content:center;border-radius:1px}
.gear{position:absolute;left:428px;top:9px;width:6px;height:6px;border-radius:50%;background:#9a9aa4}
.assess{position:absolute;left:115px;top:351px;width:463px;height:145px;background:var(--lilac);border-radius:2px;overflow:hidden}

/* library */
.lib-head{position:absolute;left:115px;top:84px;width:467px;height:51px;background:linear-gradient(90deg,#fde3bf,#fdebd6);border-radius:4px}
.tabbar{position:absolute;left:115px;top:148px;width:467px;height:27px;background:var(--indigo);color:#fff;font-size:7.5px}
.tabbar span{position:absolute;top:9px;transform:translateX(-50%);white-space:nowrap}
.tabbar i{position:absolute;left:0;bottom:0;width:137px;height:3px;background:var(--orange)}
.cluster-grid{position:absolute;left:115px;top:175px;width:467px;height:325px;background:var(--lilac)}
.cluster{position:absolute;width:58px;height:57px;background:#fff;border-radius:2px;box-shadow:0 2px 5px rgba(0,0,0,.14);text-align:center}
.cluster-icon{width:30px;height:30px;border-radius:50%;background:var(--purple);margin:5px auto 0;display:flex;align-items:center;justify-content:center}
.cluster-icon i{width:12px;height:12px;border:1.5px solid #fff;border-radius:3px;display:block}
.cluster p{font-size:3.8px;line-height:1.25;margin-top:4px;padding:0 3px}
</style>
</head>
<body>
<div class="board">

  <!-- Sign in -->
  <section class="signin shadow">
    <div class="signin-bar"></div>
    <div class="brand" style="left:47px;top:20px"><span class="brand-dot"></span>ROUTEWISE</div>
    <div class="btn" style="left:431px;top:20px;width:63px;background:var(--teal)">SIGN UP</div>
    <div class="btn" style="left:503px;top:20px;width:63px;background:var(--violet)">SIGN IN</div>
    <h1 class="signin-title">SIGN IN WITH YOUR<br>SCHOOL ACCOUNT</h1>
    <p class="tiny" style="left:0;top:128px;width:290px">LOG IN WITH YOUR</p>
    <div class="provider" style="left:43px;width:102px"><i></i>Campus Acount</div>
    <div class="provider" style="left:154px;width:93px"><i style="border-radius:1px"></i>District Acount</div>
    <p class="tiny" style="left:0;top:179px;width:290px">OR CONTINUE WITH</p>
    <div class="field" style="top:199px">Email here</div>
    <div class="field" style="top:240px">Password</div>
    <p class="tiny" style="left:0;top:279px;width:290px">FORGOT YOUR PASSWORD?</p>
    <div class="art" role="img" aria-label="Illustration of a student climbing a rising blue arrow among gears, a rocket and a light bulb" style="left:262px;top:70px;width:329px;height:263px;background:radial-gradient(ellipse at 55% 60%,#c9ccf6 0%,#e6e7fb 45%,#fff 75%)"></div>
  </section>

  <!-- Dashboard (large) -->
  <section class="dash app shadow" style="left:65px;top:698px">
    <div class="app-main" style="left:99px;top:44px"></div>
    <div class="brand" style="left:23px;top:16px"><span class="brand-dot"></span>ROUTEWISE</div>
    <div class="search" style="left:306px;top:16px;width:145px">Search<svg viewBox="0 0 10 10"><circle cx="4" cy="4" r="3" fill="none" stroke="#333" stroke-width="1.3"/><path d="M6.2 6.2 9 9" stroke="#333" stroke-width="1.3"/></svg></div>
    <div class="avatar" role="img" aria-label="User profile photo" style="left:470px;top:12px"></div>
    <div class="email" style="left:498px;top:17px">sam@mapleed.org</div>
    <div class="nav-item is-active" style="top:87px"><svg viewBox="0 0 10 10"><path d="M1 5 5 1.5 9 5v4H1z" fill="none" stroke="#fff"/></svg>HOME</div>
    <div class="nav-item" style="top:119px"><svg viewBox="0 0 10 10"><path d="M1 4 5 2l4 2-4 2z M3 5v2.5h4V5" fill="none" stroke="#fff"/></svg>CAREER TOOLS</div>
    <div class="nav-item" style="top:144px"><svg viewBox="0 0 10 10"><rect x="2" y="1" width="6" height="8" fill="none" stroke="#fff"/></svg>CLASSES</div>
    <div class="nav-item" style="top:172px"><svg viewBox="0 0 10 10"><rect x="1" y="1" width="8" height="8" fill="none" stroke="#fff"/><path d="M3 7V5M5 7V3M7 7V4" stroke="#fff"/></svg>ASSESSMENTS</div>

    <h2 class="section-title" style="left:133px;top:63px">Lesson Overview</h2>
    <div class="stat stat--done" style="left:127px"><span class="stat-label">Completed Lessons</span><span class="stat-value">35</span>
      <div class="stat-ring"><svg viewBox="0 0 56 56"><circle cx="28" cy="28" r="24" fill="none" stroke="#fff" stroke-width="3"/><circle cx="28" cy="28" r="24" fill="none" stroke="var(--orange)" stroke-width="3" stroke-dasharray="101 151" transform="rotate(-90 28 28)" stroke-linecap="round"/></svg><span>67%</span></div></div>
    <div class="stat stat--taken" style="left:287px"><span class="stat-label">Lesson Taken</span><span class="stat-value">23</span>
      <div class="stat-ring"><svg viewBox="0 0 56 56"><circle cx="28" cy="28" r="24" fill="none" stroke="#fff" stroke-width="3"/><circle cx="28" cy="28" r="24" fill="none" stroke="var(--indigo)" stroke-width="3" stroke-dasharray="56 151" transform="rotate(90 28 28)" stroke-linecap="round"/></svg><span>37%</span></div></div>
    <div class="stat stat--passed" style="left:444px"><span class="stat-label" style="top:7px">Passed Lessons</span><span class="stat-value">12</span>
      <div class="stat-ring"><svg viewBox="0 0 56 56"><circle cx="28" cy="28" r="24" fill="none" stroke="#fff" stroke-width="3"/><circle cx="28" cy="28" r="24" fill="none" stroke="var(--teal-ring)" stroke-width="3" stroke-dasharray="56 151" transform="rotate(90 28 28)" stroke-linecap="round"/></svg><span>37%</span></div></div>

    <h2 class="section-title" style="left:133px;top:207px">Career Spotlight</h2>
    <h2 class="section-title" style="left:363px;top:207px">Learnig Video</h2>
    <article class="spotlight">
      <div class="spotlight-head">Plumber, Pipeline, &amp; Steamfitters<svg width="12" height="12" viewBox="0 0 12 12"><circle cx="6" cy="6" r="5.2" fill="none" stroke="#fff" stroke-width=".8"/><path d="M3.5 6h5M6.5 4l2 2-2 2" fill="none" stroke="#fff" stroke-width=".8"/></svg></div>
      <div class="spotlight-body">
        <h4>What they do</h4>
        <p>Plumbers install and repair the pipes that carry water and gas through homes and buildings. They read plans, fit fixtures, test systems and fix leaks on site.</p>
        <h4 style="margin-top:9px">Career Earnings</h4>
        <div class="earnings"><div>Low End<b>$33,460</b></div><div>Median<b>$56,330</b></div><div>High End<b>$98,990</b></div></div>
      </div>
    </article>
    <div class="video" role="img" aria-label="Video still of a plumber working on pipes under a sink"><svg class="play" viewBox="0 0 46 46"><circle cx="23" cy="23" r="21" fill="rgba(0,0,0,.25)" stroke="#fff" stroke-width="2.5"/><path d="M18 14v18l15-9z" fill="#fff"/></svg></div>

    <h2 class="section-title" style="left:133px;top:402px">Classes</h2>
    <span class="abs" style="left:525px;top:399px;font-size:9px">View All</span>
    <div class="class-card" style="left:127px"><span class="class-teacher">&#9679; Math Teacher</span><span class="class-period">Period 1</span><div class="folder-back"></div><div class="folder-paper paper-teal">8th Grade Math /<br>Pre-Algebra</div><div class="folder-front">GO TO CLASS</div></div>
    <div class="class-card" style="left:280px"><span class="class-teacher">&#9679; Math Teacher</span><span class="class-period">Period 6</span><div class="folder-back"></div><div class="folder-paper paper-indigo" style="padding-top:16px">Algebra 1</div><div class="folder-front">GO TO CLASS</div></div>
    <div class="class-card" style="left:440px"><span class="class-teacher">&#9679; Math Teacher</span><span class="class-period">Period 5</span><div class="folder-back"></div><div class="folder-paper paper-teal" style="padding-top:12px">Algebra 2</div><div class="folder-front">GO TO CLASS</div></div>

    <h2 class="section-title" style="left:133px;top:609px">Upcoming Lessions</h2>
    <table class="lesson-table">
      <tr><th style="width:91px">CLASS</th><th style="width:193px;padding-left:48px">LESSONS</th><th>DUE</th></tr>
      <tr><td>Period 1</td><td style="padding-left:48px">1.1 - Translations</td><td>October 15th at 11.59PM</td></tr>
      <tr><td>Period 2</td><td style="padding-left:48px">2.1 - Operations with Rational Numbers</td><td>October 15th at 11.59PM</td></tr>
      <tr><td>Period 1</td><td style="padding-left:48px">3.1 - Parallel Lines and Transversals</td><td>October 15th at 11.59PM</td></tr>
      <tr><td>Period 1</td><td style="padding-left:48px">4.1 - Angle Relationship in Triangles</td><td>October 15th at 11.59PM</td></tr>
    </table>
  </section>

  <!-- Dashboard (compact) -->
  <section class="dash dash--compact app shadow" style="left:680px;top:317px">
    <div class="app-main" style="left:99px;top:44px"></div>
    <div class="brand" style="left:23px;top:16px"><span class="brand-dot"></span>ROUTEWISE</div>
    <div class="search" style="left:306px;top:16px;width:145px">Search<svg viewBox="0 0 10 10"><circle cx="4" cy="4" r="3" fill="none" stroke="#333" stroke-width="1.3"/><path d="M6.2 6.2 9 9" stroke="#333" stroke-width="1.3"/></svg></div>
    <div class="avatar" role="img" aria-label="User profile photo" style="left:470px;top:12px"></div>
    <div class="email" style="left:498px;top:17px">sam@mapleed.org</div>
    <div class="nav-item is-active" style="top:87px"><svg viewBox="0 0 10 10"><path d="M1 5 5 1.5 9 5v4H1z" fill="none" stroke="#fff"/></svg>HOME</div>
    <div class="nav-item" style="top:119px"><svg viewBox="0 0 10 10"><path d="M1 4 5 2l4 2-4 2z M3 5v2.5h4V5" fill="none" stroke="#fff"/></svg>CAREER TOOLS</div>
    <div class="nav-item" style="top:144px"><svg viewBox="0 0 10 10"><rect x="2" y="1" width="6" height="8" fill="none" stroke="#fff"/></svg>CLASSES</div>
    <div class="nav-item" style="top:172px"><svg viewBox="0 0 10 10"><rect x="1" y="1" width="8" height="8" fill="none" stroke="#fff"/><path d="M3 7V5M5 7V3M7 7V4" stroke="#fff"/></svg>ASSESSMENTS</div>

    <h2 class="section-title" style="left:133px;top:63px">Lesson Overview</h2>
    <div class="stat stat--done" style="left:127px"><span class="stat-label">Completed Lessons</span><span class="stat-value">35</span>
      <div class="stat-ring"><svg viewBox="0 0 56 56"><circle cx="28" cy="28" r="24" fill="none" stroke="#fff" stroke-width="3"/><circle cx="28" cy="28" r="24" fill="none" stroke="var(--orange)" stroke-width="3" stroke-dasharray="101 151" transform="rotate(-90 28 28)" stroke-linecap="round"/></svg><span>67%</span></div></div>
    <div class="stat stat--taken" style="left:287px"><span class="stat-label">Lesson Taken</span><span class="stat-value">23</span>
      <div class="stat-ring"><svg viewBox="0 0 56 56"><circle cx="28" cy="28" r="24" fill="none" stroke="#fff" stroke-width="3"/><circle cx="28" cy="28" r="24" fill="none" stroke="var(--indigo)" stroke-width="3" stroke-dasharray="56 151" transform="rotate(90 28 28)" stroke-linecap="round"/></svg><span>37%</span></div></div>
    <div class="stat stat--passed" style="left:444px"><span class="stat-label" style="top:7px">Passed Lessons</span><span class="stat-value">12</span>
      <div class="stat-ring"><svg viewBox="0 0 56 56"><circle cx="28" cy="28" r="24" fill="none" stroke="#fff" stroke-width="3"/><circle cx="28" cy="28" r="24" fill="none" stroke="var(--teal-ring)" stroke-width="3" stroke-dasharray="56 151" transform="rotate(90 28 28)" stroke-linecap="round"/></svg><span>37%</span></div></div>

    <h2 class="section-title" style="left:133px;top:207px">Career Spotlight</h2>
    <h2 class="section-title" style="left:363px;top:207px">Learnig Video</h2>
    <article class="spotlight">
      <div class="spotlight-head">Plumber, Pipeline, &amp; Steamfitters<svg width="12" height="12" viewBox="0 0 12 12"><circle cx="6" cy="6" r="5.2" fill="none" stroke="#fff" stroke-width=".8"/><path d="M3.5 6h5M6.5 4l2 2-2 2" fill="none" stroke="#fff" stroke-width=".8"/></svg></div>
      <div class="spotlight-body">
        <h4>What they do</h4>
        <p>Plumbers install and repair the pipes that carry water and gas through homes and buildings. They read plans, fit fixtures, test systems and fix leaks on site.</p>
        <h4 style="margin-top:9px">Career Earnings</h4>
        <div class="earnings"><div>Low End<b>$33,460</b></div><div>Median<b>$56,330</b></div><div>High End<b>$98,990</b></div></div>
      </div>
    </article>
    <div class="video" role="img" aria-label="Video still of a plumber working on pipes under a sink"><svg class="play" viewBox="0 0 46 46"><circle cx="23" cy="23" r="21" fill="rgba(0,0,0,.25)" stroke="#fff" stroke-width="2.5"/><path d="M18 14v18l15-9z" fill="#fff"/></svg></div>

    <h2 class="section-title" style="left:133px;top:402px">Classes</h2>
    <span class="abs" style="left:525px;top:399px;font-size:9px">View All</span>
    <div class="class-card" style="left:127px"><span class="class-teacher">&#9679; Math Teacher</span><span class="class-period">Period 1</span><div class="folder-back"></div><div class="folder-paper paper-teal">8th Grade Math /<br>Pre-Algebra</div><div class="folder-front">GO TO CLASS</div></div>
    <div class="class-card" style="left:280px"><span class="class-teacher">&#9679; Math Teacher</span><span class="class-period">Period 6</span><div class="folder-back"></div><div class="folder-paper paper-indigo" style="padding-top:16px">Algebra 1</div><div class="folder-front">GO TO CLASS</div></div>
    <div class="class-card" style="left:440px"><span class="class-teacher">&#9679; Math Teacher</span><span class="class-period">Period 5</span><div class="folder-back"></div><div class="folder-paper paper-teal" style="padding-top:12px">Algebra 2</div><div class="folder-front">GO TO CLASS</div></div>

    <h2 class="section-title" style="left:133px;top:609px">Upcoming Lessions</h2>
    <table class="lesson-table">
      <tr><th style="width:91px">CLASS</th><th style="width:193px;padding-left:48px">LESSONS</th><th>DUE</th></tr>
      <tr><td>Period 1</td><td style="padding-left:48px">1.1 - Translations</td><td>October 15th at 11.59PM</td></tr>
      <tr><td>Period 2</td><td style="padding-left:48px">2.1 - Operations with Rational Numbers</td><td>October 15th at 11.59PM</td></tr>
      <tr><td>Period 1</td><td style="padding-left:48px">3.1 - Parallel Lines and Transversals</td><td>October 15th at 11.59PM</td></tr>
      <tr><td>Period 1</td><td style="padding-left:48px">4.1 - Angle Relationship in Triangles</td><td>October 15th at 11.59PM</td></tr>
    </table>
  </section>

  <!-- Class detail -->
  <section class="app shadow" style="left:1267px;top:315px;width:601px;height:523px">
    <div class="app-main" style="left:101px;top:45px"></div>
    <div class="brand" style="left:26px;top:15px"><span class="brand-dot"></span>ROUTEWISE</div>
    <div class="search" style="left:310px;top:16px;width:147px">Search<svg viewBox="0 0 10 10"><circle cx="4" cy="4" r="3" fill="none" stroke="#333" stroke-width="1.3"/><path d="M6.2 6.2 9 9" stroke="#333" stroke-width="1.3"/></svg></div>
    <div class="avatar" role="img" aria-label="User profile photo" style="left:474px;top:12px"></div>
    <div class="email" style="left:504px;top:17px">sam@mapleed.org</div>
    <div class="nav-item" style="top:88px"><svg viewBox="0 0 10 10"><path d="M1 5 5 1.5 9 5v4H1z" fill="none" stroke="#fff"/></svg>HOME</div>
    <div class="nav-item" style="top:121px"><svg viewBox="0 0 10 10"><path d="M1 4 5 2l4 2-4 2z M3 5v2.5h4V5" fill="none" stroke="#fff"/></svg>CAREER TOOLS</div>
    <div class="nav-item is-active" style="top:146px;left:6px"><svg viewBox="0 0 10 10"><rect x="2" y="1" width="6" height="8" fill="none" stroke="#fff"/></svg>CLASSES</div>
    <div class="nav-item" style="top:174px"><svg viewBox="0 0 10 10"><rect x="1" y="1" width="8" height="8" fill="none" stroke="#fff"/><path d="M3 7V5M5 7V3M7 7V4" stroke="#fff"/></svg>ASSESSMENTS</div>

    <div class="back" style="left:128px;top:67px"><svg viewBox="0 0 14 6"><path d="M14 3H1M3.5 .5 1 3l2.5 2.5" fill="none" stroke="#222" stroke-width=".8"/></svg>BACK TO ALL CLASSES</div>
    <div class="course-head"></div>
    <div class="abs" style="left:130px;top:94px;font-size:6.5px;font-weight:500">&#9679; Math Teacher</div>
    <div class="abs" style="left:130px;top:107px;font-size:5px">Period 5</div>
    <div class="abs" style="left:130px;top:118px;font-size:5px">8th Grade Math / Pre-Algebra</div>
    <div class="ghost-btn" style="left:384px"><svg viewBox="0 0 10 10"><circle cx="3.5" cy="4" r="1.6" fill="none" stroke="#333" stroke-width=".7"/><circle cx="6.5" cy="4" r="1.6" fill="none" stroke="#333" stroke-width=".7"/><path d="M1 8c.5-2 4.5-2 5 0M4 8c.5-2 4.5-2 5 0" fill="none" stroke="#333" stroke-width=".7"/></svg>Class Roaster</div>
    <div class="ghost-btn" style="left:473px"><svg viewBox="0 0 10 10"><circle cx="5" cy="5" r="3.5" fill="none" stroke="#333" stroke-width=".8" stroke-dasharray="1.3 .7"/><circle cx="5" cy="5" r="1.4" fill="none" stroke="#333" stroke-width=".7"/></svg>Class Settings</div>
    <div class="abs" style="left:130px;top:145px;font-size:6.5px;font-weight:500">Lessons</div>
    <div class="abs" style="left:130px;top:157px;width:30px;height:1.5px;background:var(--orange)"></div>
    <div class="abs" style="left:208px;top:145px;font-size:6.5px;font-weight:500">Scores</div>

    <div class="lessons-panel"></div>
    <div class="abs" style="left:131px;top:174px;width:0;height:0;border-left:3.5px solid transparent;border-right:3.5px solid transparent;border-top:5px solid #999"></div>
    <div class="abs" style="left:148px;top:172px;font-size:8px;font-weight:500">Upcoming Lessions</div>
    <div class="btn" style="left:507px;top:166px;width:57px;height:19px;background:var(--orange);font-size:5px;gap:3px"><span style="display:inline-block;width:7px;height:7px;border-radius:50%;background:#fff;color:var(--orange);font-size:7px;line-height:6px;text-align:center">+</span>Add Lessons</div>
    <div class="abs" style="left:117px;top:190px;width:459px;height:1px;background:#e3e3e8"></div>
    <div class="lesson-row" style="top:196px"><span class="lesson-thumb"></span><span class="lesson-name">1.1: TRANSLATION</span><span class="lesson-desc">Career Spotlight: Aerospace Engineers, Civil Engineers, Aerospace Technicians, Carpenters, Interior Decorato</span><span class="lesson-due">Due: 10/15 at 11.59PM</span><span class="begin">Begin Lesson</span><span class="gear"></span></div>
    <div class="lesson-row" style="top:225px"><span class="lesson-thumb"></span><span class="lesson-name">1.1: TRANSLATION</span><span class="lesson-desc">Career Spotlight: Aerospace Engineers, Civil Engineers, Aerospace Technicians, Carpenters, Interior Decorato</span><span class="lesson-due">Due: 10/15 at 11.59PM</span><span class="begin">Begin Lesson</span><span class="gear"></span></div>
    <div class="lesson-row" style="top:254px"><span class="lesson-thumb"></span><span class="lesson-name">1.1: TRANSLATION</span><span class="lesson-desc">Career Spotlight: Aerospace Engineers, Civil Engineers, Aerospace Technicians, Carpenters, Interior Decorato</span><span class="lesson-due">Due: 10/15 at 11.59PM</span><span class="begin">Begin Lesson</span><span class="gear"></span></div>
    <div class="lesson-row" style="top:283px"><span class="lesson-thumb"></span><span class="lesson-name">1.1: TRANSLATION</span><span class="lesson-desc">Career Spotlight: Aerospace Engineers, Civil Engineers, Aerospace Technicians, Carpenters, Interior Decorato</span><span class="lesson-due">Due: 10/15 at 11.59PM</span><span class="begin">Begin Lesson</span><span class="gear"></span></div>
    <div class="lesson-row" style="top:310px"><span class="lesson-thumb"></span><span class="lesson-name">1.1: TRANSLATION</span><span class="lesson-desc">Career Spotlight: Aerospace Engineers, Civil Engineers, Aerospace Technicians, Carpenters, Interior Decorato</span><span class="lesson-due">Due: 10/15 at 11.59PM</span><span class="begin">Begin Lesson</span><span class="gear"></span></div>

    <div class="assess">
      <h3 class="abs" style="left:21px;top:19px;font-size:15px;font-weight:700">Routewise Assessments</h3>
      <p class="abs" style="left:21px;top:37px;font-size:7px;font-weight:700">Looking for your upcoming Routewise Assessments?</p>
      <p class="abs" style="left:21px;top:57px;width:182px;font-size:5.5px;line-height:1.2">The Routewise Assessments are designed to be taken 3 times a year at the beginning of the year, the middle of the year, and the end of the year. Navigate over to Routewise Assessments now to see what's coming up!</p>
      <div class="btn" style="left:23px;top:100px;width:78px;height:20px;background:var(--orange);font-size:5px">GO THERE NOW</div>
      <div class="art" role="img" aria-label="Illustration of two students talking beside a checklist and score gauge" style="left:218px;top:9px;width:235px;height:136px;background:radial-gradient(ellipse at 50% 70%,#c5c8f4 0%,#d8d9f6 50%,var(--lilac) 80%)"></div>
    </div>
  </section>

  <!-- Career library -->
  <section class="app shadow" style="left:1268px;top:875px;width:606px;height:529px">
    <div class="app-main" style="left:101px;top:45px"></div>
    <div class="brand" style="left:26px;top:15px"><span class="brand-dot"></span>ROUTEWISE</div>
    <div class="search" style="left:312px;top:16px;width:147px">Search<svg viewBox="0 0 10 10"><circle cx="4" cy="4" r="3" fill="none" stroke="#333" stroke-width="1.3"/><path d="M6.2 6.2 9 9" stroke="#333" stroke-width="1.3"/></svg></div>
    <div class="avatar" role="img" aria-label="User profile photo" style="left:478px;top:12px"></div>
    <div class="email" style="left:508px;top:17px">sam@mapleed.org</div>
    <div class="nav-item" style="top:89px"><svg viewBox="0 0 10 10"><path d="M1 5 5 1.5 9 5v4H1z" fill="none" stroke="#fff"/></svg>HOME</div>
    <div class="nav-item is-active" style="top:122px;left:6px"><svg viewBox="0 0 10 10"><path d="M1 4 5 2l4 2-4 2z M3 5v2.5h4V5" fill="none" stroke="#fff"/></svg>CAREER TOOLS</div>
    <div class="nav-item" style="top:148px"><svg viewBox="0 0 10 10"><rect x="2" y="1" width="6" height="8" fill="none" stroke="#fff"/></svg>CLASSES</div>
    <div class="nav-item" style="top:176px"><svg viewBox="0 0 10 10"><rect x="1" y="1" width="8" height="8" fill="none" stroke="#fff"/><path d="M3 7V5M5 7V3M7 7V4" stroke="#fff"/></svg>ASSESSMENTS</div>

    <div class="back" style="left:129px;top:64px"><svg viewBox="0 0 14 6"><path d="M14 3H1M3.5 .5 1 3l2.5 2.5" fill="none" stroke="#222" stroke-width=".8"/></svg>BACK TO ALL CLASSES</div>
    <div class="lib-head"></div>
    <h3 class="abs" style="left:124px;top:94px;font-size:16px;font-weight:700">Career Library</h3>
    <p class="abs" style="left:124px;top:116px;font-size:7.3px">Explore careers to find jobs that match your interests and skill set.</p>
    <div class="abs" style="left:396px;top:105px;width:178px;height:13px;background:#fff;border-radius:7px;font-size:4.5px;padding:4px 0 0 10px;box-shadow:0 1px 3px rgba(0,0,0,.15)">Search Career<span class="abs" style="right:0;top:0;width:30px;height:13px;border-radius:7px;background:var(--indigo);color:#fff;font-size:4px;text-align:center;line-height:13px">Search</span></div>
    <nav class="tabbar"><span style="left:79px">Career cluster</span><span style="left:234px">Values and Interests</span><span style="left:389px">Education zone</span><i></i></nav>
    <div class="cluster-grid"></div>
    <div class="cluster" style="left:168px;top:208px"><div class="cluster-icon"><i></i></div><p>Agriculture, Food &amp; Natural Resources</p></div>
    <div class="cluster" style="left:244px;top:208px"><div class="cluster-icon"><i></i></div><p>Architecture &amp; Construction</p></div>
    <div class="cluster" style="left:320px;top:208px"><div class="cluster-icon"><i></i></div><p>Arts, Audio/Video Technology &amp; Communications</p></div>
    <div class="cluster" style="left:396px;top:208px"><div class="cluster-icon"><i></i></div><p>Business &amp; Management</p></div>
    <div class="cluster" style="left:472px;top:208px"><div class="cluster-icon"><i></i></div><p>Education &amp; Training</p></div>
    <div class="cluster" style="left:168px;top:292px"><div class="cluster-icon"><i></i></div><p>Finance</p></div>
    <div class="cluster" style="left:244px;top:292px"><div class="cluster-icon"><i></i></div><p>Government &amp; Public Administration</p></div>
    <div class="cluster" style="left:320px;top:292px"><div class="cluster-icon"><i></i></div><p>Hospitality &amp; Tourism</p></div>
    <div class="cluster" style="left:396px;top:292px"><div class="cluster-icon"><i></i></div><p>Human Services</p></div>
    <div class="cluster" style="left:472px;top:292px"><div class="cluster-icon"><i></i></div><p>Information Technology</p></div>
    <div class="cluster" style="left:168px;top:382px"><div class="cluster-icon"><i></i></div><p>Manufacturing</p></div>
    <div class="cluster" style="left:244px;top:382px"><div class="cluster-icon"><i></i></div><p>Marketing, Sales &amp; Services</p></div>
    <div class="cluster" style="left:320px;top:382px"><div class="cluster-icon"><i></i></div><p>Transportation distribution &amp; Logistics</p></div>
    <div class="cluster" style="left:396px;top:382px"><div class="cluster-icon"><i></i></div><p>Health and Science</p></div>
  </section>

</div>
</body>
</html>
```